Cobaltine Pilates Summer Promotions

I would like to create 2 x A6 one-side flyers for my Cobaltine Pilates private yoga summer promotions. I have 2 promotions available (bring a friend for free + 4 for price of 3 package). I would like the 2 flyers to look similar in style but would like them to look different enough so they catch the eye of the customer that there are 2 different promotions available.
Attached is my PowerPoint "versions" which I created myself but would like them to be taken to the next level for professionalism and design. You do not have to follow this layout - this was just my (non-designer-mind) ideas.
The wording in the PowerPoint must be included. You are free to use all my logos and images attached in whichever way you think works best. Feel free to use other yoga/scenic imagery you find which may be suitable.

Please stick to these font options:
Logo font: Amatic
Main text font: Raleway

Colour palette in the branding guidelines attached.

Font styles to use
Other font styles liked:
• Amatic + Raleway

Requirements
Must have
• Colour palette as per attached branding guidelines
• Fonts Amatic + Raleway
• Same design style but 2 different layouts for the 2 different promotions
• My logo must be included
• Call to action to book a session
• Wording as per PowerPoint attached
• Contact details - email, phone and website
Nice to have
• Optional other relevant yoga/lavender themed imagery
• Picture of me (to build familiarity with customers)

```html
<!DOCTYPE html>
<html lang="en">
<head>
<meta charset="utf-8">
<title>Cobaltine Pilates – Private Yoga Classes</title>
<link href="https://fonts.googleapis.com/css2?family=Amatic+SC:wght@400;700&family=Raleway:ital,wght@0,400;0,500;0,600;0,700;1,600&display=swap" rel="stylesheet">
<style>
  :root {
    --backdrop: #ececec;
    --paper: #ffffff;
    --lavender: #a892c8;
    --plum: #6e4d92;
    --text-grey: #8c8c8c;
    --photo-warm: #e9ddd6;
    --photo-plum: #a07a8c;
    --photo-floor: #c9a27a;
  }
  * { box-sizing: border-box; margin: 0; padding: 0; }
  html, body { width: 1200px; height: 898px; overflow: hidden; }
  body { background: var(--backdrop); font-family: "Raleway", sans-serif; }

  .flyer {
    position: absolute; left: 302px; top: 28px;
    width: 596px; height: 842px;
    background: var(--paper);
    overflow: hidden;
    box-shadow: 0 4px 14px rgba(0,0,0,0.12);
  }
  .flyer__photo {
    position: absolute; left: 0; top: 90px; width: 360px; height: 752px;
    background:
      linear-gradient(90deg, rgba(255,255,255,0) 55%, #fff 100%),
      linear-gradient(180deg, var(--photo-warm) 0%, var(--photo-plum) 45%, #3a3540 70%, var(--photo-floor) 100%);
  }
  .flyer__photo-fade {
    position: absolute; left: 0; top: 90px; width: 360px; height: 752px;
    background: linear-gradient(180deg, #fff 0%, rgba(255,255,255,0) 12%, rgba(255,255,255,0) 60%, rgba(255,255,255,0.85) 78%, rgba(255,255,255,0.2) 100%);
  }

  .brand {
    position: absolute; left: 300px; top: 40px; width: 220px;
    display: flex; align-items: center; justify-content: center; gap: 8px;
  }
  .brand__dot { width: 12px; height: 12px; border-radius: 50%; background: var(--lavender); }
  .brand__name { font-family: "Amatic SC", cursive; font-size: 30px; color: var(--plum); font-weight: 400; }

  .content { position: absolute; left: 268px; top: 110px; width: 300px; }
  .headline { font-family: "Amatic SC", cursive; font-weight: 700; color: var(--lavender); font-size: 44px; line-height: 1; }
  .subhead { font-family: "Amatic SC", cursive; font-weight: 700; color: var(--plum); font-size: 27px; line-height: 1.1; margin-bottom: 12px; }
  .body p { font-size: 12.5px; line-height: 1.6; color: var(--text-grey); text-align: justify; margin-bottom: 10px; }

  .prices {
    position: relative; margin: 26px 18px 18px; padding: 20px 12px 12px;
    border: 1px solid var(--lavender); text-align: center;
  }
  .prices__badge {
    position: absolute; top: -13px; left: 50%; transform: translateX(-50%);
    width: 26px; height: 26px; border-radius: 50%; background: var(--lavender);
  }
  .prices li { list-style: none; font-size: 12.5px; line-height: 1.55; color: var(--plum); font-weight: 500; }

  .details { text-align: center; font-size: 12.5px; line-height: 1.5; color: var(--text-grey); }
  .details strong { color: var(--plum); font-weight: 600; }
  .details em { color: var(--plum); font-weight: 600; }

  .cta { margin-top: 26px; font-size: 13px; font-weight: 700; color: var(--plum); text-transform: uppercase; text-align: center; letter-spacing: 0.2px; }
  .contacts { list-style: none; margin: 10px 0 0 44px; }
  .contacts li { display: flex; align-items: center; gap: 8px; font-size: 12.5px; color: var(--text-grey); line-height: 1.7; }
  .contacts svg { width: 16px; height: 16px; flex: none; }
</style>
</head>
<body>
  <main class="flyer">
    <div class="flyer__photo" role="img" aria-label="Photo of the instructor smiling, seated cross-legged on a yoga mat with palms together in a bright studio"></div>
    <div class="flyer__photo-fade"></div>

    <header class="brand">
      <span class="brand__dot"></span>
      <span class="brand__name">Cobaltine Pilates</span>
    </header>

    <section class="content">
      <h1 class="headline">Private Yoga Classes</h1>
      <h2 class="subhead">Bring a friend for free this summer!</h2>

      <div class="body">
        <p>Going to a new yoga class can be a little intimidating. Where do I put my mat? Does it matter I can't even touch my toes? What language will they speak? I get it. I've been there.</p>
        <p>So instead, how about trying private yoga classes? We can practice at the best time for your schedule. And make it even more fun by doing it with your friend.</p>
        <p>This summer if you book a private class with me you can now do just that, and bring a friend along for free!</p>
      </div>

      <ul class="prices">
        <span class="prices__badge"></span>
        <li>60 minutes – 120fr (60fr each!)</li>
        <li>75 minutes – 150fr (75fr each!)</li>
        <li>90 minutes – 180fr (90fr each!)</li>
      </ul>

      <div class="details">
        <p><strong>Offer period:</strong> <em>July to September 2017</em></p>
        <p>Location: Let's discuss! I have options to use studio spaces or we can do it at yours' or your friend's home</p>
      </div>

      <p class="cta">Get in touch to book your session!</p>
      <ul class="contacts">
        <li>
          <svg viewBox="0 0 16 16"><circle cx="8" cy="8" r="8" fill="var(--plum)"/><circle cx="8" cy="8" r="4.5" fill="none" stroke="#fff" stroke-width="1"/><path d="M3.5 8h9M8 3.5v9" stroke="#fff" stroke-width="1"/></svg>
          www.cobaltine.studio
        </li>
        <li>
          <svg viewBox="0 0 16 16"><circle cx="8" cy="8" r="8" fill="var(--plum)"/><path d="M5.5 4.5l1.5 0 .7 2-1 .8a5 5 0 0 0 2 2l.8-1 2 .7v1.5c-3.5.5-6.5-2.5-6-6z" fill="#fff"/></svg>
          0712 345 678
        </li>
        <li>
          <svg viewBox="0 0 16 16"><circle cx="8" cy="8" r="8" fill="var(--plum)"/><rect x="4" y="5.5" width="8" height="5.5" fill="#fff"/><path d="M4 5.5l4 3 4-3" fill="none" stroke="var(--plum)" stroke-width="0.8"/></svg>
          hello@cobaltinestudio.com
        </li>
      </ul>
    </section>
  </main>
</body>
</html>
```